Company letter head and business card for new Indian Pharmaceutical Export company.

We need a letterhead and business card design for an Indian Pharmaceutical Export company.

The letter head needs to contain the following information.
Verona Healthline Pvt. Ltd.
Office No 4837 Plot No 52, Kestrel Heights, RT Lane, 400517, Maharashtra, India.
Email: info@verona-healthline.example
Phone: +91-8213460592
CIN: U58213MH2025PTC719264
GSTIN: (This number is still pending, we will add later)

The business card needs to contain:
Address:
Verona Healthline Pvt. Ltd.
Office No 4837 Plot No52, Kestrel Heights, RT Lane, 400517, MH, India.
Email: tobias@verona-healthline.example
Phone: +49-17638421956
Name on card: Tobias Wendlinger
Position: Director

The design for the letter head and business card should be simple but trustworthy.
Please use only Green and blue, same as in the attached logo.

```html
<!DOCTYPE html>
<html lang="en">
<head>
<meta charset="utf-8">
<title>Verona Healthline – Business Card</title>
<link rel="stylesheet" href="https://fonts.googleapis.com/css2?family=Montserrat:wght@800&family=Arimo:wght@400;700&display=swap">
<style>
  :root {
    --blue: #0a5da3;
    --blue-band: #1f74bf;
    --green: #8bc43f;
    --ink: #4a4a4a;
    --rule: #555555;
    --page: #c9c9c9;
    --white: #ffffff;
    --faint-blue: #e6eef6;
  }
  html, body {
    margin: 0;
    padding: 0;
    width: 1125px;
    height: 1200px;
    overflow: hidden;
    background: var(--page);
  }
  .canvas {
    position: relative;
    width: 1125px;
    height: 1200px;
  }
  .card {
    position: absolute;
    left: 150px;
    width: 825px;
    height: 472px;
    border-radius: 20px;
    overflow: hidden;
    background: var(--white);
    box-shadow: 0 3px 8px rgba(0,0,0,0.35);
  }
  .card--front { top: 98px; }
  .card--back { top: 631px; background: var(--blue); }

  .card svg { position: absolute; left: 0; top: 0; }

  .brand-name {
    position: absolute;
    font-family: "Montserrat", sans-serif;
    font-weight: 800;
    white-space: nowrap;
    margin: 0;
  }
  .card--front .brand-name {
    left: 39px;
    top: 243px;
    font-size: 24px;
    color: var(--blue);
  }
  .contact {
    position: absolute;
    left: 39px;
    top: 288px;
    font-family: "Arimo", Arial, sans-serif;
    font-size: 22px;
    color: var(--ink);
    line-height: 29px;
  }
  .contact-row { display: flex; align-items: center; gap: 8px; white-space: nowrap; }
  .contact-row svg { position: static; }
  .divider {
    position: absolute;
    left: 39px;
    top: 354px;
    width: 427px;
    border-top: 2px solid var(--rule);
  }
  .address {
    position: absolute;
    left: 39px;
    top: 362px;
    font-family: "Arimo", Arial, sans-serif;
    font-size: 22px;
    line-height: 30px;
    color: var(--ink);
    margin: 0;
    font-style: normal;
  }
  .person {
    position: absolute;
    right: 40px;
    top: 35px;
    text-align: right;
    font-family: "Arimo", Arial, sans-serif;
  }
  .person-name {
    margin: 0;
    font-size: 26px;
    font-weight: 700;
    color: var(--blue);
    line-height: 30px;
  }
  .person-role {
    margin: 0;
    font-size: 22px;
    color: var(--green);
    line-height: 30px;
  }
  .accent-bar {
    position: absolute;
    right: 0;
    top: 36px;
    width: 13px;
    height: 65px;
    background: var(--green);
  }
  .card--back .brand-name {
    right: 40px;
    top: 318px;
    font-size: 36px;
    color: var(--white);
  }
</style>
</head>
<body>
<main class="canvas">

  <section class="card card--front" aria-label="Business card front">
    <svg width="825" height="472" viewBox="0 0 825 472" aria-hidden="true">
      <circle class="decor-circle" cx="676" cy="310" r="165" fill="none" stroke="var(--faint-blue)" stroke-width="14"/>
      <circle class="brand-mark" cx="137" cy="137" r="88" fill="none" stroke="var(--blue)" stroke-width="12"/>
      <path class="band band--blue" d="M0 450 H570 Q590 450 602 472 H0 Z" fill="var(--blue-band)"/>
      <path class="band band--green" d="M735 472 Q765 450 800 450 H825 V472 Z" fill="var(--green)"/>
    </svg>

    <p class="brand-name">Verona Healthline</p>

    <div class="contact">
      <div class="contact-row">
        <svg width="20" height="16" viewBox="0 0 20 16" aria-hidden="true">
          <path d="M1 6 Q10 -1 19 6 L16 8 L13 5 H7 L4 8 Z M4 9 H16 L17 15 H3 Z" fill="var(--green)"/>
        </svg>
        <span>+49-17638421956</span>
      </div>
      <div class="contact-row">
        <svg width="20" height="16" viewBox="0 0 20 16" aria-hidden="true">
          <path d="M1 6 L10 0 L19 6 V16 H1 Z" fill="var(--green)"/>
          <path d="M1 6 L10 12 L19 6" fill="none" stroke="var(--white)" stroke-width="1.5"/>
        </svg>
        <span>tobias@verona-healthline.example</span>
      </div>
    </div>

    <div class="divider"></div>

    <address class="address">Office No 4837 Plot No52<br>Kestrel Heights, RT Lane, 400517, MH, India</address>

    <div class="person">
      <p class="person-name">TOBIAS WENDLINGER</p>
      <p class="person-role">Director</p>
    </div>
    <div class="accent-bar"></div>
  </section>

  <section class="card card--back" aria-label="Business card back">
    <svg width="825" height="472" viewBox="0 0 825 472" aria-hidden="true">
      <rect class="field field--green" x="0" y="0" width="330" height="472" fill="var(--green)"/>
      <circle class="field field--blue" cx="335" cy="236" r="270" fill="var(--blue)"/>
      <path class="arc arc--white" d="M185 10 A270 270 0 0 0 200 472" fill="none" stroke="var(--white)" stroke-width="16"/>
    </svg>
    <p class="brand-name">Verona Healthline</p>
  </section>

</main>
</body>
</html>
```